Corvell Executive Search - New Business Card Design Project

We are an executive search firm called Corvell Executive Search based in the UK. We require a custom design for a business card. We're looking to convey a professional service to executives for executive search recruitment services. In terms of colours, we like dark blues and grays (maybe even silver incorporated somewhere if we go for a foiled type of card) but we're open to your artistic flare. See our current logo in attachments. We are totally open on design so long as the design is slick and professional.
Updates

Thanks for all your contributions of various designs. I have to say the quality of work has been amazing which is going to make our job quite difficult in the coming days on making a decision. Thanks to you all that have taken the time to submit designs thus far. We'll keep on reviewing and try to narrow down our selection as soon as possible.

Target Market(s)

Executive Search

Industry/Entity Type

Recruitment

Contact Information for Business Card

Corvell Executive Search,
Exclusively Sourcing & Hiring Senior Leaders
Dominic Haverley, Managing Director,
07742 318906
0117 468 2917
dominic@corvellexecutive.example
corvellexecutive.example
47 Linden Court, Marsh Lane, Bristol, BS9 7QT

Font styles to use
Sans Serif
Other font styles liked:
• Roboto (which is used in our logo)

Requirements
Must have
• Our logo (It has a subtle fade on it from #02071d at top to #333649 at bottom)
• The logo can be on one side or both sides
• Must be elegant and professional
• We have 2nd slogan CONSULT | INSPIRE | INNOVATE | DELIVER which can be incorporated into the card
Nice to have
• Use of blues and grey colours
• Compatible with similar styling to our website corvellexecutive.example
Should not have
• Must not be overly brash
• Must not contain cartoon characters

```html
<!DOCTYPE html>
<html lang="en">
<head>
<meta charset="utf-8">
<title>Corvell Executive Search – Business Card</title>
<link href="https://fonts.googleapis.com/css2?family=Roboto:wght@400;500;700&display=swap" rel="stylesheet">
<style>
  :root {
    --backdrop: #646569;
    --card: #ffffff;
    --navy: #1b2338;
    --brand-blue: #1a6fb5;
    --ink: #222326;
    --tagline-grey: #8c8c8e;
    --divider-grey: #8a8a8a;
  }
  * { margin: 0; padding: 0; box-sizing: border-box; }
  html, body {
    width: 1200px; height: 1200px; overflow: hidden;
    background: var(--backdrop);
    font-family: "Roboto", Arial, sans-serif;
  }
  .sheet { position: relative; width: 1200px; height: 1200px; }
  .card {
    position: absolute; left: 200px; width: 800px; height: 500px;
    background: var(--card); overflow: hidden;
  }
  .card--front { top: 70px; }
  .card--back { top: 620px; }

  /* Front */
  .tagline {
    position: absolute; left: 70px; top: 118px; width: 280px;
    text-align: center; font-weight: 500; font-size: 21px; line-height: 28px;
    color: var(--tagline-grey);
    text-shadow: 1px 1px 2px rgba(0,0,0,0.35);
  }
  .brand { position: absolute; display: flex; flex-direction: column; }
  .brand--front { right: 60px; top: 40px; align-items: flex-end; }
  .brand__square { background: var(--navy); }
  .brand--front .brand__square { width: 150px; height: 150px; }
  .brand__name {
    font-weight: 500; color: var(--navy); text-transform: uppercase;
    letter-spacing: 0.5px;
  }
  .brand--front .brand__name { font-size: 18px; margin-top: 12px; }

  .person { position: absolute; left: 64px; top: 268px; }
  .person__name { font-size: 30px; color: var(--brand-blue); font-weight: 400; line-height: 36px; }
  .person__role { font-size: 20px; color: var(--ink); margin-top: 4px; }
  .rule {
    position: absolute; left: 64px; right: 58px; top: 346px; height: 4px;
    background: var(--brand-blue);
  }
  .contacts { position: absolute; top: 366px; list-style: none; font-size: 20px; color: var(--ink); }
  .contacts li { display: flex; align-items: center; height: 34px; gap: 10px; white-space: nowrap; }
  .contacts--left { left: 64px; }
  .contacts--right { right: 58px; text-align: right; }
  .contacts--right li { justify-content: flex-end; }
  .icon { width: 18px; height: 18px; flex: none; fill: var(--brand-blue); }
  .icon--blank { visibility: hidden; }

  /* Back */
  .brand--back { left: 0; right: 0; top: 62px; align-items: center; }
  .brand--back .brand__square { width: 220px; height: 220px; }
  .brand--back .brand__name { font-size: 30px; margin-top: 22px; }
  .slogan {
    position: absolute; left: 0; right: 0; top: 412px;
    text-align: center; font-weight: 700; font-size: 23px;
    color: var(--brand-blue); letter-spacing: 0.5px;
  }
  .slogan__bar { color: var(--divider-grey); font-weight: 400; margin: 0 12px; }
</style>
</head>
<body>
<main class="sheet">

  <section class="card card--front" aria-label="Card front">
    <p class="tagline">Exclusively Sourcing<br>&amp;<br>Hiring Senior Leaders</p>

    <div class="brand brand--front">
      <div class="brand__square"></div>
      <span class="brand__name">Corvell Executive Search</span>
    </div>

    <div class="person">
      <h1 class="person__name">Dominic Haverley</h1>
      <p class="person__role">Managing Director</p>
    </div>
    <div class="rule"></div>

    <ul class="contacts contacts--left">
      <li>
        <svg class="icon" viewBox="0 0 24 24"><path d="M6.6 10.8a15.1 15.1 0 0 0 6.6 6.6l2.2-2.2a1 1 0 0 1 1-.25 11.4 11.4 0 0 0 3.6.57 1 1 0 0 1 1 1V20a1 1 0 0 1-1 1A17 17 0 0 1 3 4a1 1 0 0 1 1-1h3.5a1 1 0 0 1 1 1c0 1.25.2 2.45.57 3.57a1 1 0 0 1-.25 1z"/></svg>
        07742 318906
      </li>
      <li>
        <svg class="icon" viewBox="0 0 24 24"><path d="M7 2h10a2 2 0 0 1 2 2v16a2 2 0 0 1-2 2H7a2 2 0 0 1-2-2V4a2 2 0 0 1 2-2zm0 3v13h10V5zm4 14.5h2v1h-2z"/></svg>
        0117 468 2917
      </li>
      <li>
        <svg class="icon" viewBox="0 0 24 24"><path d="M2 5h20v14H2zm2 2v.5l8 5.5 8-5.5V7z"/></svg>
        dominic@corvellexecutive.example
      </li>
    </ul>

    <ul class="contacts contacts--right">
      <li>
        47 Linden Court, Marsh Lane
        <svg class="icon" viewBox="0 0 24 24"><path d="M12 2a7 7 0 0 0-7 7c0 5.2 7 13 7 13s7-7.8 7-13a7 7 0 0 0-7-7zm0 4a3 3 0 1 1 0 6 3 3 0 0 1 0-6z"/></svg>
      </li>
      <li>
        Bristol, BS9 7QT
        <svg class="icon icon--blank" viewBox="0 0 24 24"></svg>
      </li>
      <li>
        corvellexecutive.example
        <svg class="icon" viewBox="0 0 24 24"><path d="M12 2a10 10 0 1 0 0 20 10 10 0 0 0 0-20zm6.9 6h-2.9a15.6 15.6 0 0 0-1.4-3.6A8 8 0 0 1 18.9 8zM12 4c.8 1.2 1.5 2.5 1.9 4h-3.8c.4-1.5 1.100-2.8 1.9-4zM4.3 14a8 8 0 0 1 0-4h3.4a16 16 0 0 0 0 4zm.8 2h2.9c.3 1.3.8 2.5 1.4 3.6A8 8 0 0 1 5.1 16zM8 8H5.1a8 8 0 0 1 4.3-3.6C8.8 5.5 8.3 6.7 8 8zm4 12c-.8-1.2-1.5-2.5-1.9-4h3.8c-.4 1.5-1.1 2.8-1.9 4zm2.3-6H9.7a14.7 14.7 0 0 1 0-4h4.6a14.7 14.7 0 0 1 0 4zm.3 5.6c.6-1.1 1.1-2.3 1.4-3.6h2.9a8 8 0 0 1-4.3 3.6zm1.7-5.6a16 16 0 0 0 0-4h3.4a8 8 0 0 1 0 4z"/></svg>
      </li>
    </ul>
  </section>

  <section class="card card--back" aria-label="Card back">
    <div class="brand brand--back">
      <div class="brand__square"></div>
      <span class="brand__name">Corvell Executive Search</span>
    </div>
    <p class="slogan">CONSULT<span class="slogan__bar">|</span>INSPIRE<span class="slogan__bar">|</span>INNOVATE<span class="slogan__bar">|</span>DELIVER</p>
  </section>

</main>
</body>
</html>
```